Editorial Website Design for High-End Custom Millwork Firm

Design (no development) for a 5-7 page website for a high-end custom architectural millwork firm. Editorial, magazine-quality aesthetic — think Dwelling Quarterly and top-tier millwork studios (Owen Tallard, Vorko). Full brief, reference sites, and project photography attached. We have uploaded a sample of our photography to use in your design. PLEASE READ PDF DOCUMENT BRIEF!!!

```html
<!DOCTYPE html>
<html lang="en">
<head>
<meta charset="utf-8">
<title>Halden Millwork — Website Design Board</title>
<link href="https://fonts.googleapis.com/css2?family=Cormorant+Garamond:ital,wght@0,400;0,500;1,400&family=Jost:wght@400;500;600&display=swap" rel="stylesheet">
<style>
:root{
  --ivory:#FAF6F1; --ivory-2:#F7F2EA; --ivory-3:#EFE7DC;
  --walnut-1:#ECDCCD; --walnut-2:#9B7351; --wood:#6B4A32; --walnut-4:#24170F;
  --brass-1:#FBF4EB; --brass-2:#CFA75F; --accent:#A47A43; --brass-4:#2D2013;
  --n-1:#FAF9F7; --n-2:#D8CDBE; --n-3:#6F6A61; --ink:#1F1E1B;
  --err-1:#FFF2EF; --err-2:#C85D4F; --err-3:#A94438;
  --ok-1:#F3F7EF; --ok-2:#789653; --ok-3:#5F7D3D;
  --footer:#2D241D; --rule:#E4DACB; --board:#B3B3B3;
  --serif:"Cormorant Garamond", Georgia, serif;
  --sans:"Jost", Arial, sans-serif;
}
*{margin:0;padding:0;box-sizing:border-box}
html,body{width:1200px;height:1200px;overflow:hidden;background:var(--board)}
.stage{position:relative;width:1932px;height:1932px;transform:scale(.621118);transform-origin:0 0;background:var(--board)}
.page{position:absolute;width:449px;background:var(--ivory);overflow:hidden;color:var(--ink);font-family:var(--sans)}
.page-flow{position:relative}
section{position:relative;width:449px;border-bottom:1px solid var(--rule)}
.a{position:absolute}
.photo{position:absolute}
.photo--kitchen{background:linear-gradient(125deg,#f3eee6 0%,#e7ddcf 45%,#c8a77f 75%,#9c7550 100%)}
.photo--workshop{background:linear-gradient(160deg,#8e8b86 0%,#bfb3a0 45%,#d8c7a6 65%,#5e5a55 100%)}
.photo--commercial{background:linear-gradient(90deg,#3e2a1e 0%,#8c6d56 45%,#6d5443 70%,#56693a 100%)}
.photo--detail{background:linear-gradient(180deg,#c2c1bf 0%,#b9b7b3 35%,#c99a66 55%,#acaaa6 100%)}
.photo--shaping{background:linear-gradient(150deg,#d9d6d1 0%,#7d8ea6 50%,#c8b08a 100%)}
.photo--assembly{background:linear-gradient(140deg,#2f2a25 0%,#8a6e52 50%,#d3b48d 100%)}
.caption{position:absolute;font-family:var(--sans);font-size:4.6px;color:var(--n-3)}
.caption--italic{font-family:var(--serif);font-style:italic;font-size:5.5px}
.eyebrow{position:absolute;font-size:4.4px;letter-spacing:.14em;color:var(--accent);text-transform:uppercase;display:flex;align-items:center;gap:8px}
.eyebrow i{display:block;height:1px;background:var(--accent);opacity:.5}
.tiny{font-size:4.6px;line-height:7.2px;color:var(--n-3)}
.serif{font-family:var(--serif);font-weight:400}

/* hero */
.hero{height:250px}
.hero-frame{left:4px;top:4px;width:441px;height:244px;border:1px solid var(--rule)}
.brand-word{font-family:var(--serif);font-size:7.5px;letter-spacing:.18em;color:var(--ink)}
.nav{right:18px;top:13px;display:flex;gap:11px;font-size:3.8px;letter-spacing:.1em;color:var(--ink)}
.nav .nav-cta{color:var(--wood)}
.vert{writing-mode:vertical-rl;transform:rotate(180deg);font-size:3.8px;letter-spacing:.16em;color:var(--accent)}
.hero-panel{left:40px;top:40px;width:146px;height:170px;background:var(--ivory)}
.hero-title{left:50px;top:43px;font-family:var(--serif);font-size:29px;line-height:26px;color:var(--ink);white-space:nowrap;letter-spacing:-.01em}
.hero-lede{left:50px;top:163px;width:100px;font-size:4.3px;line-height:6.8px;color:var(--ink)}
.btn{font-size:3.6px;letter-spacing:.14em;text-transform:uppercase}
.btn--solid{left:50px;top:193px;width:50px;height:12px;background:var(--wood);color:var(--ivory);display:flex;align-items:center;justify-content:center}
.btn--link{left:111px;top:197px;color:var(--wood)}
.hero-strip{left:8px;top:232px;width:433px;display:flex;align-items:center;gap:16px;font-family:var(--serif);font-size:4.6px;letter-spacing:.2em;color:var(--n-3);text-transform:uppercase}
.hero-strip i{flex:1;height:1px;background:var(--rule)}

/* intro */
.intro{height:222px}
.quote{left:26px;top:58px;width:122px;font-family:var(--serif);font-size:13.5px;line-height:18.3px;color:var(--ink)}
.facts{left:330px;top:68px;width:99px;list-style:none}
.facts li{font-size:5.2px;height:22.4px;padding-top:2px;border-bottom:1px solid var(--rule);color:var(--ink)}

/* work */
.work{height:300px}
.work-title{left:14px;top:24px;font-family:var(--serif);font-size:15px;line-height:18px;color:var(--ink)}
.crumbs{left:14px;top:280px;width:421px;padding-top:4px;font-size:4px;color:var(--n-3);word-spacing:1px}

/* capabilities */
.capabilities{height:215px}
.cap-title{left:18px;top:52px;font-family:var(--serif);font-size:21px;color:var(--ink)}
.cap-lede{left:18px;top:87px;width:112px}
.cap-list{left:176px;top:33px;width:258px;list-style:none;border-top:1px solid var(--rule)}
.cap-list li{position:relative;height:25px;border-bottom:1px solid var(--rule);font-size:5.6px;display:flex;align-items:center;color:var(--ink)}
.cap-list li b{font-weight:400;color:var(--accent);width:34px;padding-left:6px}
.cap-note{left:176px;top:187px;font-size:3.8px;color:var(--n-3)}

/* process */
.process{height:268px}
.proc-title{left:19px;top:26px;font-family:var(--serif);font-size:19px;line-height:21px;color:var(--ink)}
.proc-lede{left:19px;top:75px;width:175px}
.steps{left:367px;top:70px;width:64px;list-style:none}
.steps li{height:39px;border-bottom:1px solid var(--rule);padding-top:2px;margin-bottom:0}
.steps li:last-child{border-bottom:none}
.steps b{display:block;font-family:var(--serif);font-weight:400;font-size:10px;color:var(--wood)}
.steps span{display:block;font-size:4px;color:var(--ink);margin-top:1px}

/* quality */
.quality{height:274px;background:#221C17;color:var(--ivory);border:none}
.q-title{left:26px;top:48px;font-family:var(--serif);font-size:30px;line-height:30px;color:var(--ivory)}
.q-sub{left:26px;top:124px;font-family:var(--serif);font-size:8.6px;color:#D9C7AA}
.q-copy{left:26px;top:143px;width:130px;font-size:5px;line-height:7.6px;color:#D8CFC3}
.q-rule-v{left:225px;top:20px;width:1px;height:184px;background:rgba(207,167,95,.35)}
.q-photo{left:245px;top:17px;width:127px;height:186px;border:2px solid #EFE7DC}
.q-meta{left:383px;top:140px;font-size:3.6px;letter-spacing:.16em;color:var(--brass-2);line-height:7px}
.q-stats{left:20px;top:220px;width:409px;height:42px;border-top:1px solid rgba(207,167,95,.3);display:flex}
.q-stats div{flex:1;display:flex;align-items:center;justify-content:center;text-align:center;font-size:4.6px;letter-spacing:.18em;line-height:7px;color:#E8DDCC;border-left:1px solid rgba(207,167,95,.3)}
.q-stats div:first-child{border-left:none}

/* cta */
.cta{height:135px}
.cta-title{left:28px;top:38px;font-family:var(--serif);font-size:24px;line-height:27px;color:var(--ink)}
.cta-box{left:302px;top:19px;width:119px;height:101px;border:1px solid var(--brass-2)}
.cta-box .tiny{position:absolute;left:13px;top:12px;width:80px;color:var(--ink)}
.cta-link{position:absolute;left:13px;top:61px;font-family:var(--serif);font-size:11px;color:var(--accent);display:flex;align-items:center;gap:5px}
.cta-tags{position:absolute;left:13px;top:84px;font-size:3px;letter-spacing:.1em;color:var(--ink)}

/* footer */
.site-footer{height:97px;background:var(--ivory-3);border:none}
.f-brand{left:28px;top:12px;font-family:var(--serif);font-size:13px;letter-spacing:.04em}
.f-place{left:28px;top:37px;font-size:3.6px;letter-spacing:.16em;line-height:8px;color:var(--ink)}
.f-col{top:14px;font-size:3.6px;line-height:9.2px;color:var(--ink)}
.f-col h4{font-weight:500;font-size:3.4px;letter-spacing:.16em;color:var(--accent)}
.f-sep{top:14px;width:1px;height:56px;background:var(--n-2)}
.f-bottom{left:28px;top:80px;width:393px;border-top:1px solid var(--n-2);padding-top:4px;display:flex;justify-content:space-between;font-size:3.5px;color:var(--ink)}

/* color library */
.library{position:absolute;left:37px;top:1590px;width:1855px;height:240px;background:#F7F4EF;font-family:var(--sans);color:#2a2622}
.library h2{position:absolute;left:31px;top:8px;font-family:var(--serif);font-weight:500;font-size:31px;color:#2a2622}
.group{position:absolute;top:46px;height:102px;border:1.5px solid #DCD6CE}
.group h3{position:absolute;left:10px;top:4px;font-size:13px;font-weight:600;letter-spacing:.03em;line-height:14px}
.group h3 span{display:block;font-weight:400;letter-spacing:0;font-size:12.5px}
.sw{position:absolute;top:37px;height:39px;border:1px solid #E1DBD2}
.sw em{position:absolute;top:47px;left:-10px;right:-10px;text-align:center;font-style:normal;font-size:11.5px}
.core{position:absolute;left:20px;top:160px;width:1814px;height:72px;border:1.5px solid #DCD6CE}
.core h3{position:absolute;left:13px;top:10px;font-size:13px;font-weight:600;letter-spacing:.03em}
.bar{position:absolute;top:6px;height:28px}
.bar em{position:absolute;top:40px;left:0;right:0;text-align:center;font-style:normal;font-size:11.5px;line-height:14px}
</style>
</head>
<body>
<div class="stage">

  <!-- Home page, upper half -->
  <div class="page" style="left:392px;top:40px;height:1252px">
    <div class="page-flow">
      <section class="hero">
        <div class="a hero-frame"></div>
        <div class="a brand-word" style="left:22px;top:12px">HALDEN MILLWORK</div>
        <nav class="a nav"><span>PROJECTS</span><span>SERVICES</span><span>ABOUT</span><span>BLOG</span><span>CONTACT</span><span class="nav-cta">START A PROJECT</span></nav>
        <div class="a vert" style="left:21px;top:34px">BRIGHTWATER, NC · EST. 1988</div>
        <div class="a" style="left:23px;top:98px;width:1px;height:118px;background:var(--rule)"></div>
        <div class="photo photo--kitchen" role="img" aria-label="Bright white kitchen with oak island and brass pendants" style="left:165px;top:30px;width:257px;height:190px"></div>
        <div class="a hero-panel"></div>
        <h1 class="a hero-title">Architectural<br>Millwork,<br>Crafted to a<br>Higher Standard</h1>
        <p class="a hero-lede">Custom architectural millwork and cabinetry for commercial interiors, luxury residences, architects, and designers.</p>
        <div class="a btn btn--solid">View Projects</div>
        <div class="a btn btn--link">Start a Conversation</div>
        <div class="a vert" style="left:430px;top:138px">GUILD QC PREMIUM GRADE</div>
        <div class="a" style="left:432px;top:203px;width:1px;height:18px;background:var(--n-3)"></div>
        <div class="a hero-strip"><i></i><span>Commercial Interiors</span><span>|</span><span>Luxury Residences</span><span>|</span><span>Custom Cabinetry</span><i></i></div>
      </section>

      <section class="intro">
        <blockquote class="a quote">“Since 1988, Halden Millwork has shaped interiors where craftsmanship is meant to be seen.”</blockquote>
        <div class="a" style="left:26px;top:205px;width:18px;height:1px;background:var(--n-2)"></div>
        <div class="photo photo--workshop" role="img" aria-label="Craftsman assembling a lattice panel at a workshop bench" style="left:154px;top:40px;width:150px;height:133px"></div>
        <ul class="a facts">
          <li>Brightwater, North Carolina</li>
          <li>Established 1988</li>
          <li>Guild QC Premium Grade</li>
          <li>70% Commercial / 30% Residential</li>
        </ul>
      </section>

      <section class="work">
        <div class="eyebrow" style="left:14px;top:11px">Selected Work <i style="width:80px"></i></div>
        <h2 class="a work-title">Commercial interiors, private residences,<br>and custom architectural details built with precision.</h2>
        <div class="photo photo--kitchen" role="img" aria-label="Residential kitchen with oak island cabinetry" style="left:14px;top:71px;width:244px;height:178px"></div>
        <div class="caption" style="left:14px;top:253px">Residential Cabinetry</div>
        <div class="photo photo--commercial" role="img" aria-label="Commercial lounge with walnut panelling and patterned screen" style="left:266px;top:71px;width:169px;height:85px"></div>
        <div class="caption" style="left:266px;top:160px">Commercial Interiors</div>
        <div class="photo photo--detail" role="img" aria-label="Grey drawer fronts with inset wood pulls" style="left:266px;top:173px;width:169px;height:76px"></div>
        <div class="caption" style="left:266px;top:254px">Custom Architectural Details</div>
        <div class="a crumbs">01 Residential Cabinetry &nbsp;&nbsp;/&nbsp;&nbsp; 02 Commercial Interiors &nbsp;&nbsp;/&nbsp;&nbsp; 03 Custom Details &nbsp;&nbsp;/&nbsp;&nbsp; 04 Built-in Millwork</div>
      </section>

      <section class="capabilities">
        <div class="eyebrow" style="left:18px;top:37px">Capabilities</div>
        <h2 class="a cap-title">What We Build</h2>
        <p class="a tiny cap-lede">From commercial interiors to finely detailed residential cabinetry, Halden Millwork carries projects from shop drawings through fabrication and installation.</p>
        <ul class="a cap-list">
          <li><b>01</b>Architectural Millwork</li>
          <li><b>02</b>Custom Cabinetry<span class="photo photo--kitchen" role="img" aria-label="Oak cabinetry detail" style="left:194px;top:3px;width:63px;height:20px"></span></li>
          <li><b>03</b>Commercial Interiors<span class="photo photo--commercial" role="img" aria-label="Commercial lounge interior" style="left:137px;top:1px;width:121px;height:22px"></span></li>
          <li><b>04</b>Residential Built-ins<span class="photo photo--detail" role="img" aria-label="Built-in drawer fronts" style="left:194px;top:3px;width:63px;height:19px"></span></li>
          <li><b>05</b>Specialty Details</li>
          <li><b>06</b>Fabrication + Installation</li>
        </ul>
        <div class="a cap-note">Designed, fabricated, finished, and installed with premium-grade standards.</div>
      </section>

      <section class="process">
        <div class="eyebrow" style="left:19px;top:11px">Craft + Process</div>
        <h2 class="a proc-title">Built by Hand,<br>Refined by Process</h2>
        <p class="a tiny proc-lede">Every project moves through a disciplined path: design review, engineering, fabrication, finishing, and installation. The work is measured, built, and checked by craftspeople before it reaches the room.</p>
        <div class="photo photo--workshop" role="img" aria-label="Shop fabrication of a lattice panel" style="left:16px;top:107px;width:198px;height:138px"></div>
        <div class="caption caption--italic" style="left:16px;top:248px">Shop fabrication</div>
        <div class="photo photo--shaping" role="img" aria-label="Worker shaping material with a power tool" style="left:221px;top:65px;width:122px;height:78px"></div>
        <div class="caption caption--italic" style="left:221px;top:146px">Material shaping</div>
        <div class="photo photo--assembly" role="img" aria-label="Worker assembling a curved wood frame" style="left:221px;top:160px;width:122px;height:85px"></div>
        <div class="caption caption--italic" style="left:221px;top:249px">Assembly detail</div>
        <ol class="a steps">
          <li><b>01</b><span>Design Review</span></li>
          <li><b>02</b><span>Engineering</span></li>
          <li><b>03</b><span>Fabrication</span></li>
          <li><b>04</b><span>Finishing</span></li>
          <li><b>05</b><span>Installation</span></li>
        </ol>
      </section>
    </div>
  </div>

  <!-- Home page, lower half -->
  <div class="page" style="left:898px;top:0;height:1070px">
    <div class="page-flow" style="top:-219px">
      <section class="work">
        <div class="photo photo--kitchen" role="img" aria-label="Residential kitchen with oak island cabinetry" style="left:14px;top:71px;width:244px;height:178px"></div>
        <div class="caption" style="left:14px;top:253px">Residential Cabinetry</div>
        <div class="photo photo--detail" role="img" aria-label="Grey drawer fronts with inset wood pulls" style="left:266px;top:173px;width:169px;height:76px"></div>
        <div class="caption" style="left:266px;top:254px">Custom Architectural Details</div>
        <div class="a crumbs">01 Residential Cabinetry &nbsp;&nbsp;/&nbsp;&nbsp; 02 Commercial Interiors &nbsp;&nbsp;/&nbsp;&nbsp; 03 Custom Details &nbsp;&nbsp;/&nbsp;&nbsp; 04 Built-in Millwork</div>
      </section>

      <section class="capabilities">
        <div class="eyebrow" style="left:18px;top:37px">Capabilities</div>
        <h2 class="a cap-title">What We Build</h2>
        <p class="a tiny cap-lede">From commercial interiors to finely detailed residential cabinetry, Halden Millwork carries projects from shop drawings through fabrication and installation.</p>
        <ul class="a cap-list">
          <li><b>01</b>Architectural Millwork</li>
          <li><b>02</b>Custom Cabinetry<span class="photo photo--kitchen" role="img" aria-label="Oak cabinetry detail" style="left:194px;top:3px;width:63px;height:20px"></span></li>
          <li><b>03</b>Commercial Interiors<span class="photo photo--commercial" role="img" aria-label="Commercial lounge interior" style="left:137px;top:1px;width:121px;height:22px"></span></li>
          <li><b>04</b>Residential Built-ins<span class="photo photo--detail" role="img" aria-label="Built-in drawer fronts" style="left:194px;top:3px;width:63px;height:19px"></span></li>
          <li><b>05</b>Specialty Details</li>
          <li><b>06</b>Fabrication + Installation</li>
        </ul>
        <div class="a cap-note">Designed, fabricated, finished, and installed with premium-grade standards.</div>
      </section>

      <section class="process">
        <div class="eyebrow" style="left:19px;top:11px">Craft + Process</div>
        <h2 class="a proc-title">Built by Hand,<br>Refined by Process</h2>
        <p class="a tiny proc-lede">Every project moves through a disciplined path: design review, engineering, fabrication, finishing, and installation. The work is measured, built, and checked by craftspeople before it reaches the room.</p>
        <div class="photo photo--workshop" role="img" aria-label="Shop fabrication of a lattice panel" style="left:16px;top:107px;width:198px;height:138px"></div>
        <div class="caption caption--italic" style="left:16px;top:248px">Shop fabrication</div>
        <div class="photo photo--shaping" role="img" aria-label="Worker shaping material with a power tool" style="left:221px;top:65px;width:122px;height:78px"></div>
        <div class="caption caption--italic" style="left:221px;top:146px">Material shaping</div>
        <div class="photo photo--assembly" role="img" aria-label="Worker assembling a curved wood frame" style="left:221px;top:160px;width:122px;height:85px"></div>
        <div class="caption caption--italic" style="left:221px;top:249px">Assembly detail</div>
        <ol class="a steps">
          <li><b>01</b><span>Design Review</span></li>
          <li><b>02</b><span>Engineering</span></li>
          <li><b>03</b><span>Fabrication</span></li>
          <li><b>04</b><span>Finishing</span></li>
          <li><b>05</b><span>Installation</span></li>
        </ol>
      </section>

      <section class="quality">
        <div class="eyebrow" style="left:26px;top:25px;color:var(--brass-2)">Quality + Legacy <i style="width:90px;background:var(--brass-2)"></i></div>
        <h2 class="a q-title">Quality is built<br>into the process.</h2>
        <p class="a q-sub">Premium-grade work, measured at every stage.</p>
        <p class="a q-copy">Halden Millwork brings certified standards, experienced craftspeople, and careful project coordination to commercial and residential interiors.</p>
        <div class="a q-rule-v"></div>
        <div class="photo photo--workshop q-photo" role="img" aria-label="Craftsman fitting a lattice panel in the shop"></div>
        <div class="a q-meta">BRIGHTWATER, NC<br><br>ESTABLISHED 1988<br><br>CERTIFIED<br>STANDARDS</div>
        <div class="a q-stats">
          <div>GUILD QC<br>PREMIUM GRADE</div>
          <div>MBE<br>CERTIFICATION</div>
          <div>ESTABLISHED<br>1988</div>
          <div>BUILT IN<br>BRIGHTWATER, NC</div>
        </div>
      </section>

      <section class="cta">
        <div class="eyebrow" style="left:28px;top:23px">Start a Project <i style="width:28px"></i></div>
        <h2 class="a cta-title">Have a project<br>that demands<br>careful execution?</h2>
        <svg class="a" style="left:140px;top:68px" width="164" height="26" viewBox="0 0 164 26"><path d="M0 23 H70 C92 23 100 3 120 3 H164" fill="none" stroke="#CFA75F" stroke-width=".8"/></svg>
        <div class="a cta-box">
          <p class="tiny">Tell us about the room, the schedule, and the level of finish required.</p>
          <div class="cta-link">Start a Project
            <svg width="16" height="6" viewBox="0 0 16 6"><path d="M0 3H15M12 .5 15 3 12 5.5" fill="none" stroke="#A47A43" stroke-width=".7"/></svg>
          </div>
          <div class="cta-tags">COMMERCIAL · RESIDENTIAL / BRIGHTWATER, NC</div>
        </div>
      </section>

      <footer class="site-footer" style="position:relative;width:449px">
        <div class="a f-brand">HALDEN MILLWORK</div>
        <div class="a f-place">BRIGHTWATER, NORTH CAROLINA<br>ESTABLISHED 1988</div>
        <div class="a f-sep" style="left:156px"></div>
        <div class="a f-col" style="left:174px"><h4>EXPLORE</h4>Projects<br>Services<br>About<br>Blog<br>Contact</div>
        <div class="a f-sep" style="left:232px"></div>
        <div class="a f-col" style="left:249px"><h4>CAPABILITIES</h4>Architectural Millwork<br>Custom Cabinetry<br>Commercial Interiors<br>Residential Built-ins</div>
        <div class="a f-sep" style="left:320px"></div>
        <div class="a f-col" style="left:338px"><h4>CREDENTIALS</h4>Guild QC Premium Grade<br>MBE Certified<br>Commercial + Residential</div>
        <div class="a f-bottom"><span>© 2026 Halden Millwork. All rights reserved.</span><span>info@haldenmillwork.com</span></div>
      </footer>
    </div>
  </div>

  <!-- Colour library -->
  <div class="library">
    <h2>Color Library</h2>

    <div class="group" style="left:23px;width:296px"><h3>PRIMARY<span>Warm Ivory</span></h3>
      <div class="sw" style="left:9px;width:79px;background:var(--ivory)"><em>#FAF6F1</em></div>
      <div class="sw" style="left:100px;width:79px;background:var(--ivory-2)"><em>#F7F2EA</em></div>
      <div class="sw" style="left:191px;width:89px;background:var(--ivory-3)"><em>#EFE7DC</em></div>
    </div>
    <div class="group" style="left:338px;width:344px"><h3>SECONDARY<span>Walnut / Wood</span></h3>
      <div class="sw" style="left:8px;width:69px;background:var(--walnut-1)"><em>#ECDCCD</em></div>
      <div class="sw" style="left:92px;width:69px;background:var(--walnut-2)"><em>#9B7351</em></div>
      <div class="sw" style="left:175px;width:68px;background:var(--wood)"><em>#6B4A32</em></div>
      <div class="sw" style="left:257px;width:64px;background:var(--walnut-4)"><em>#24170F</em></div>
    </div>
    <div class="group" style="left:710px;width:327px"><h3>ACCENT<span>Aged Brass</span></h3>
      <div class="sw" style="left:8px;width:69px;background:var(--brass-1)"><em>#FBF4EB</em></div>
      <div class="sw" style="left:92px;width:65px;background:var(--brass-2)"><em>#CFA75F</em></div>
      <div class="sw" style="left:172px;width:64px;background:var(--accent)"><em>#A47A43</em></div>
      <div class="sw" style="left:250px;width:62px;background:var(--brass-4)"><em>#2D2013</em></div>
    </div>
    <div class="group" style="left:1051px;width:287px"><h3>NEUTRAL<span>Editorial Charcoal</span></h3>
      <div class="sw" style="left:7px;width:57px;background:var(--n-1)"><em>#FAF9F7</em></div>
      <div class="sw" style="left:78px;width:57px;background:var(--n-2)"><em>#D8CDBE</em></div>
      <div class="sw" style="left:148px;width:57px;background:var(--n-3)"><em>#6F6A61</em></div>
      <div class="sw" style="left:218px;width:57px;background:var(--ink)"><em>#1F1E1B</em></div>
    </div>
    <div class="group" style="left:1366px;width:210px"><h3>ERROR<span>Muted Clay Red</span></h3>
      <div class="sw" style="left:7px;width:55px;background:var(--err-1)"><em>#FFF2EF</em></div>
      <div class="sw" style="left:76px;width:55px;background:var(--err-2)"><em>#C85D4F</em></div>
      <div class="sw" style="left:144px;width:56px;background:var(--err-3)"><em>#A94438</em></div>
    </div>
    <div class="group" style="left:1610px;width:224px"><h3>SUCCESS<span>Deep Olive</span></h3>
      <div class="sw" style="left:9px;width:59px;background:var(--ok-1)"><em>#F3F7EF</em></div>
      <div class="sw" style="left:83px;width:58px;background:var(--ok-2)"><em>#789653</em></div>
      <div class="sw" style="left:153px;width:58px;background:var(--ok-3)"><em>#5F7D3D</em></div>
    </div>

    <div class="core"><h3>CORE USAGE</h3>
      <div class="bar" style="left:193px;width:257px;background:var(--ivory);border:1px solid #E1DBD2"><em>Background<br>#FAF6F1</em></div>
      <div class="bar" style="left:522px;width:234px;background:var(--ink)"><em>Text<br>#1F1E1B</em></div>
      <div class="bar" style="left:846px;width:227px;background:var(--wood)"><em>Wood<br>#6B4A32</em></div>
      <div class="bar" style="left:1162px;width:224px;background:var(--accent)"><em>Accent<br>#A47A43</em></div>
      <div class="bar" style="left:1484px;width:224px;background:var(--footer)"><em>Footer<br>#2D241D</em></div>
    </div>
  </div>

</div>
</body>
</html>
```